Daniel Fordyce Psychotherapy Business Card Design Project

I need a welcoming business card for a Somatic Psychotherapy private practice based in Melbourne, Australia. I help individual clients to work through issues in their life that are inhibiting achieving their full potential. I would like a san serif font and the oculars are:
blue: R:37 G:61 B:95 C:93 M:77 Y:38 K:28
orange: R:241 G:103 B:43 C:0 M:74 Y:93 K:0
The final design should communicate warm, welcoming and safe environment in which clients are supported to grow. It should also convey a collaborative approach to achieve success between me (the therapist) and the client. The uploaded file is my new logo. Also an organic look and feel while maintaining professionalism and a clean, simple look is sought after.
In addition to the logo my details are:
Daniel Fordyce
Psychotherapist
B.Arts., Grad Dip. T&D., Dip.Som.Psych, MRTOB, MFLENG
0417 552 908
dfordyce@danielfordyce.com.au
www.danielfordyce.com.au
Psychotherapy Clients
Environment

```html
<!DOCTYPE html>
<html lang="en">
<head>
<meta charset="utf-8">
<title>Daniel Fordyce Psychotherapy – Business Card</title>
<link rel="stylesheet" href="https://fonts.googleapis.com/css2?family=Arimo:wght@400;700&display=swap">
<style>
  :root {
    --brand-blue: #253d5f;
    --brand-orange: #f1672b;
    --card-light: #ffffff;
    --card-mid: #ececec;
    --card-edge: #c9c9c9;
    --text-on-orange: #ffffff;
  }
  * { margin: 0; padding: 0; box-sizing: border-box; }
  html, body {
    width: 1200px;
    height: 686px;
    overflow: hidden;
    background: #ffffff;
  }
  .card {
    position: relative;
    width: 1200px;
    height: 686px;
    overflow: hidden;
    font-family: "Arimo", Arial, Helvetica, sans-serif;
    background: radial-gradient(ellipse 75% 80% at 38% 45%, var(--card-light) 0%, var(--card-mid) 55%, var(--card-edge) 100%);
  }
  .wave {
    position: absolute;
    inset: 0;
    width: 1200px;
    height: 686px;
  }
  .brand-name {
    position: absolute;
    left: 34px;
    top: 34px;
    font-size: 38px;
    font-weight: 400;
    line-height: 1.1;
    color: var(--brand-blue);
  }
  .credentials {
    position: absolute;
    left: 34px;
    top: 196px;
    list-style: none;
    color: var(--brand-blue);
    font-size: 37px;
    line-height: 51px;
  }
  .identity {
    position: absolute;
    left: 560px;
    width: 560px;
    top: 214px;
    text-align: center;
  }
  .identity-name {
    font-size: 76px;
    font-weight: 400;
    color: var(--brand-blue);
    line-height: 1;
  }
  .identity-role {
    margin-top: 10px;
    font-size: 38px;
    color: var(--brand-orange);
    line-height: 1;
    transform: translateX(-10px);
  }
  .contact {
    position: absolute;
    right: 12px;
    bottom: 12px;
    text-align: right;
    color: var(--text-on-orange);
  }
  .contact-phone {
    font-size: 31px;
    line-height: 40px;
  }
  .contact-web {
    font-size: 22px;
    line-height: 28px;
    letter-spacing: 0.5px;
    text-transform: uppercase;
  }
</style>
</head>
<body>
  <div class="card">
    <svg class="wave" viewBox="0 0 1200 686" aria-hidden="true">
      <path fill="var(--brand-blue)" d="M0 542 C 260 610, 720 565, 1200 352 L1200 686 L0 686 Z"/>
      <path fill="var(--brand-orange)" d="M0 566 C 270 634, 740 592, 1200 378 L1200 686 L0 686 Z"/>
    </svg>

    <p class="brand-name">Daniel Fordyce<br>Psychotherapy</p>

    <ul class="credentials">
      <li>B.Arts.</li>
      <li>Grad Dip. T&amp;D.</li>
      <li>Dip.Som.Psych</li>
      <li>MRTOB</li>
      <li>MFLENG</li>
    </ul>

    <div class="identity">
      <h1 class="identity-name">Daniel Fordyce</h1>
      <p class="identity-role">Psychotherapist</p>
    </div>

    <div class="contact">
      <p class="contact-phone">Phone: 0417 552 908</p>
      <p class="contact-web">www.danielfordyce.com.au</p>
    </div>
  </div>
</body>
</html>
```